Harbor Fieldworks (Business Card Design)

Need business cards designed. Something modern, chic, and sleek. Mabye the back of the card should be the navy blue that is in the logo and then just the logo on the back.

Target Market(s)

Those in the hotel, office, and renovation industry

Contact Information for Business Card

1. Logo 2. Dorian Velasko 3. CEO/Founder 4. Phone: (833) HarbFld / (833) 427-2353 5. Email: dorian@theharborfieldworks.com 6. Website: www.theharborfieldworks.com

Font styles to use
Other font styles liked:
• Look at the logo font and base the font for everything else off of that.

Colors
0054AA
0677BA
7BADD7
CADEEF
E8F1F8

Requirements
Must have
• Colors that are associated in the logo
Nice to have
• Sleek modern clean and chic design.

```html
<!DOCTYPE html>
<html lang="en">
<head>
<meta charset="utf-8">
<title>Harbor Fieldworks — Business Card</title>
<link rel="stylesheet" href="https://fonts.googleapis.com/css2?family=Bebas+Neue&family=Montserrat:wght@600&family=Poppins:wght@400&display=swap">
<style>
  :root {
    --backdrop: #8a8a8a;
    --card-white: #ffffff;
    --navy: #101a40;
    --steel: #5f86ab;
    --gold: #c9962e;
    --ink: #131c44;
    --grey-text: #6b6b6b;
  }
  * { margin: 0; padding: 0; box-sizing: border-box; }
  html, body { width: 1200px; height: 959px; overflow: hidden; }
  body { background: var(--backdrop); position: relative; }

  .card {
    position: absolute;
    left: 295px;
    width: 612px;
    height: 351px;
    box-shadow: 0 3px 8px rgba(0,0,0,0.25);
  }
  .card-front { top: 103px; background: var(--card-white); }
  .card-back  { top: 499px; background: var(--navy); overflow: hidden; }

  .identity {
    position: absolute;
    right: calc(612px - 235px);
    top: 146px;
    text-align: right;
  }
  .person-name {
    font-family: "Bebas Neue", sans-serif;
    font-size: 37px;
    line-height: 1;
    color: var(--ink);
    letter-spacing: 0.3px;
    white-space: nowrap;
  }
  .person-role {
    font-family: "Poppins", sans-serif;
    font-size: 14px;
    line-height: 1;
    color: var(--gold);
    margin-top: 5px;
  }
  .divider {
    position: absolute;
    left: 253px;
    top: 146px;
    width: 2px;
    height: 58px;
    background: var(--gold);
  }
  .contact-list {
    position: absolute;
    left: 270px;
    top: 144px;
    list-style: none;
    font-family: "Poppins", sans-serif;
    font-size: 14.5px;
    color: var(--grey-text);
  }
  .contact-list li {
    display: flex;
    align-items: center;
    height: 22px;
    white-space: nowrap;
  }
  .contact-list svg { width: 13px; height: 13px; margin-right: 4px; flex: none; fill: var(--ink); }

  .pattern-area {
    position: absolute;
    left: 0; top: 18px;
    width: 400px; height: 333px;
    background: linear-gradient(135deg, var(--steel) 0%, rgba(95,134,171,0.55) 45%, var(--navy) 85%);
    clip-path: polygon(0 20%, 45% 0, 100% 100%, 0 100%);
    opacity: 0.85;
  }
  .brand {
    position: absolute;
    left: 400px;
    top: 168px;
    width: 160px;
    text-align: center;
    color: var(--card-white);
    font-family: "Montserrat", sans-serif;
    font-weight: 600;
  }
  .brand-square {
    width: 14px; height: 14px;
    background: var(--card-white);
    margin: 0 auto 18px;
  }
  .brand-name {
    font-size: 19px;
    letter-spacing: 1.5px;
    line-height: 1.25;
    text-transform: uppercase;
  }
</style>
</head>
<body>
  <section class="card card-front">
    <div class="identity">
      <h1 class="person-name">Dorian Velasko</h1>
      <p class="person-role">CEO/Founder</p>
    </div>
    <div class="divider"></div>
    <ul class="contact-list">
      <li>
        <svg viewBox="0 0 24 24" aria-hidden="true"><path d="M6.6 10.8a15.1 15.1 0 0 0 6.6 6.6l2.2-2.2c.3-.3.7-.4 1-.2 1.1.4 2.3.6 3.6.6.6 0 1 .4 1 1V20c0 .6-.4 1-1 1A17 17 0 0 1 3 4c0-.6.4-1 1-1h3.5c.6 0 1 .4 1 1 0 1.3.2 2.5.6 3.6.1.3 0 .7-.2 1z"/></svg>
        (833) HarbFld / (833) 427-2353
      </li>
      <li>
        <svg viewBox="0 0 24 24" aria-hidden="true"><path d="M2 5h20v14H2z M2 5l10 8 10-8" fill="none" stroke="#131c44" stroke-width="2.5"/></svg>
        dorian@theharborfieldworks.com
      </li>
      <li>
        <svg viewBox="0 0 24 24" aria-hidden="true"><g fill="none" stroke="#131c44" stroke-width="2"><circle cx="12" cy="12" r="9.5"/><ellipse cx="12" cy="12" rx="4" ry="9.5"/><path d="M2.5 12h19M4 7h16M4 17h16"/></g></svg>
        www.theharborfieldworks.com
      </li>
    </ul>
  </section>

  <section class="card card-back">
    <div class="pattern-area" role="img" aria-label="Large decorative geometric pattern in steel blue fading into navy"></div>
    <div class="brand">
      <div class="brand-square"></div>
      <p class="brand-name">Harbor<br>Fieldworks</p>
    </div>
  </section>
</body>
</html>
```